Company Real Estate Site Needs A Face Lift

I need a new website for the recent company I formed: Voska Real Estate.
You can use my agent website WWW.PALMIROQ.COM to see the style/brand I already have. I will have areas for Searching for homes on IDX, etc.
I really like this site:
http://www.cranfeltmanorhomes.com/
I have attached my logo as well

Industry/Entity Type

Real Estate

Colors
0255a3
ffffff
cee9f5

```html
<!DOCTYPE html>
<html lang="en">
<head>
<meta charset="utf-8">
<title>Voska Real Estate</title>
<link href="https://fonts.googleapis.com/css2?family=Source+Sans+3:wght@400;600;700&display=swap" rel="stylesheet">
<style>
:root{
  --brand:#0f55a0;
  --brand-light:#cee9f5;
  --white:#ffffff;
  --ink:#5a5a5a;
  --red:#f04d44;
  --peach:#fed497;
  --salmon:#f4937a;
  --olive:#b3943c;
  --gold:#f6c22f;
  --brown:#6b3d10;
  --footer:#050505;
}
*{box-sizing:border-box;margin:0;padding:0}
html,body{width:1200px;height:821px;overflow:hidden;background:var(--white)}
body{font-family:"Source Sans 3",sans-serif;position:relative}
.site{position:relative;width:1200px;height:821px;overflow:hidden}
.header-bg{position:absolute;left:0;top:0;width:1200px;height:130px}
.logo{position:absolute;left:20px;top:30px;display:flex;align-items:center;gap:10px;color:var(--white)}
.logo-mark{width:34px;height:34px;border-radius:50%;background:var(--white);opacity:.9}
.logo-name{font-weight:700;font-size:24px;line-height:1;letter-spacing:1px}
.logo-sub{font-weight:700;font-size:13px;letter-spacing:2px;margin-top:4px}
.contact{position:absolute;right:135px;top:16px;font-size:14.5px;font-weight:600;color:var(--ink)}
.contact a{color:var(--brand);text-decoration:none}
.contact .sep{color:#bbb;margin:0 7px}
.badge{position:absolute;top:8px;height:30px;background:#5b93cf;border-radius:4px}
.badge.one{left:1081px;width:58px}
.badge.two{left:1150px;width:30px;background:var(--brand);border:2px solid #5b93cf}
.nav{position:absolute;right:19px;top:49px;height:35px;display:flex;align-items:center;gap:23px}
.nav a{color:var(--brand);text-decoration:none;font-size:16px;font-weight:600}
.search{position:absolute;left:664px;top:97px;width:267px;height:24px;border:1px solid #3b78bd;background:var(--brand);display:flex}
.search span{flex:1;color:#d6e6f5;font-size:12px;padding:4px 10px}
.search i{width:37px;border-left:1px solid #3b78bd;background:#e9f1f9;display:flex;align-items:center;justify-content:center}
.social{position:absolute;left:950px;top:96px;display:flex;gap:9px}
.social b{width:25px;height:25px;background:var(--white);border-radius:2px;display:flex;align-items:center;justify-content:center}
.hero{position:absolute;left:0;top:130px;width:1200px;height:639px;
  background:
    radial-gradient(ellipse 520px 150px at 560px 330px,rgba(225,222,205,.9),rgba(225,222,205,0) 70%),
    radial-gradient(ellipse 260px 320px at 1120px 250px,rgba(70,58,45,.75),rgba(70,58,45,0) 75%),
    linear-gradient(180deg,#e4e7e6 0%,#d3d4ce 22%,#b9b6a6 45%,#c7c2b0 58%,#8c7d66 74%,#4e3d2c 90%,#33261b 100%)}
.arrow{position:absolute;top:296px}
.arrow.left{left:18px}
.arrow.right{right:18px}
.shade{position:absolute;left:0;top:557px;width:1200px;height:212px;background:rgba(40,30,20,.45)}
.panel{position:absolute;top:569px;width:281px;height:188px;padding:17px 19px}
.panel h2{font-size:16.5px;font-weight:600;line-height:1.2}
.welcome{left:19px;background:var(--red);color:var(--white)}
.welcome p{font-size:11.8px;line-height:18.8px;margin-top:12px}
.welcome p a{color:#ffd1cc;text-decoration:none}
.video{left:312px;background:var(--peach)}
.video h2{color:var(--brown);text-transform:uppercase}
.thumb{position:absolute;top:52px;width:112px;height:116px;border:2px solid var(--white)}
.thumb.a{left:19px;background:linear-gradient(180deg,#8fa1cf,#9a7a66 60%,#4a3a33)}
.thumb.b{left:151px;background:linear-gradient(180deg,#f1f1f1,#b05a3f 55%,#7a3b2b)}
.thumb svg{position:absolute;left:36px;top:38px}
.mapsearch{left:607px;background:var(--salmon);color:var(--white)}
.mapsearch h2{text-transform:uppercase}
.map{position:absolute;left:18px;top:71px;width:245px;height:99px;border:1px solid var(--white);background:linear-gradient(135deg,#e5e6da,#c9d6e6)}
.cities{left:900px;background:var(--olive);padding:0}
.tabs{display:flex;height:40px}
.tab{padding:9px 11px;font-size:17px;font-weight:600;text-transform:uppercase}
.tab.active{color:var(--white)}
.tab.other{color:var(--gold);background:#a5862f;border-left:1px solid #c6a856}
.city-photo{position:absolute;left:19px;top:64px;width:102px;height:105px;border:1px solid var(--white);background:linear-gradient(180deg,#4a4d9c,#6b3b34 50%,#2c2430)}
.cities p{position:absolute;left:139px;top:62px;width:130px;font-size:13.5px;line-height:19.5px;color:var(--white);font-weight:600}
.footer{position:absolute;left:0;top:769px;width:1200px;height:52px;background:var(--footer);color:var(--white);font-size:14.5px;font-weight:700}
.footer span{position:absolute;top:17px;display:flex;align-items:center;gap:6px}
</style>
</head>
<body>
<div class="site">
  <svg class="header-bg" viewBox="0 0 1200 130" aria-hidden="true">
    <rect width="1200" height="130" fill="#ffffff"/>
    <polygon points="222,0 236,0 285,49 1200,49 1200,84 305,84" fill="#cee9f5"/>
    <polygon points="0,0 218,0 305,84 1200,84 1200,130 0,130" fill="#0f55a0"/>
  </svg>
  <div class="logo">
    <div class="logo-mark"></div>
    <div><div class="logo-name">VOSKA</div><div class="logo-sub">REAL ESTATE</div></div>
  </div>
  <div class="contact">CALL: <a href="#">304-555-0192</a><span class="sep">|</span>EMAIL: <a href="#">hello@voskarealty.com</a></div>
  <div class="badge one"></div>
  <div class="badge two"></div>
  <nav class="nav">
    <a href="#">Home</a><a href="#">Buy</a><a href="#">Sell</a><a href="#">Tours</a><a href="#">Testimonials</a><a href="#">Blog</a><a href="#">Resources</a><a href="#">Search Homes</a><a href="#">Contact</a>
  </nav>
  <div class="search"><span>Search</span><i><svg width="16" height="16" viewBox="0 0 16 16"><circle cx="6" cy="6" r="4.5" fill="none" stroke="#0f55a0" stroke-width="2"/><line x1="9.5" y1="9.5" x2="15" y2="15" stroke="#0f55a0" stroke-width="2.5"/></svg></i></div>
  <div class="social">
    <b><svg width="15" height="15" viewBox="0 0 16 16"><path d="M2 3h12v8H7l-3 3v-3H2z" fill="#0f55a0"/></svg></b>
    <b><svg width="15" height="15" viewBox="0 0 16 16"><rect x="1" y="3" width="14" height="10" fill="#0f55a0"/><polyline points="1,3 8,9 15,3" fill="none" stroke="#fff" stroke-width="1.5"/></svg></b>
    <b><svg width="15" height="15" viewBox="0 0 16 16"><rect x="1" y="4" width="10" height="8" rx="1" fill="#0f55a0"/><polygon points="11,8 15,5 15,11" fill="#0f55a0"/></svg></b>
    <b><svg width="15" height="15" viewBox="0 0 16 16"><circle cx="5" cy="5" r="2.5" fill="#0f55a0"/><circle cx="11" cy="5" r="2.5" fill="#0f55a0"/><rect x="1.5" y="9" width="6" height="6" fill="#0f55a0"/><rect x="8.5" y="9" width="6" height="6" fill="#0f55a0"/></svg></b>
    <b><svg width="15" height="15" viewBox="0 0 16 16"><circle cx="3" cy="13" r="2" fill="#0f55a0"/><path d="M1 7a8 8 0 0 1 8 8M1 2a13 13 0 0 1 13 13" fill="none" stroke="#0f55a0" stroke-width="2"/></svg></b>
    <b><svg width="16" height="16" viewBox="0 0 16 16"><polygon points="8,1 10,6 15,6 11,9.5 12.5,15 8,11.5 3.5,15 5,9.5 1,6 6,6" fill="none" stroke="#0f55a0" stroke-width="1.4"/></svg></b>
    <b><svg width="16" height="16" viewBox="0 0 16 16"><circle cx="8" cy="8" r="4.5" fill="none" stroke="#0f55a0" stroke-width="3" stroke-dasharray="2.4 1.2"/><circle cx="8" cy="8" r="2" fill="none" stroke="#0f55a0" stroke-width="1.4"/></svg></b>
  </div>

  <div class="hero" role="img" aria-label="Bright modern living room with a sofa and a large window overlooking a city skyline"></div>
  <svg class="arrow left" width="38" height="108" viewBox="0 0 38 108" aria-hidden="true"><polyline points="36,0 2,54 36,108" fill="none" stroke="#0f55a0" stroke-width="2"/></svg>
  <svg class="arrow right" width="38" height="108" viewBox="0 0 38 108" aria-hidden="true"><polyline points="2,0 36,54 2,108" fill="none" stroke="#0f55a0" stroke-width="2"/></svg>
  <div class="shade"></div>

  <section class="panel welcome">
    <h2>Welcome to VOSKA REAL ESTATE</h2>
    <p>Whether you are a 1st time buyer or a home buying expert of Voska Real Estate , you will be presented with many difficult choices that requires representation. If you want to avoid the pitfalls and aggravation often accompanied with buying a home, it may be in your ... <a href="#">[read more]</a></p>
  </section>
  <section class="panel video">
    <h2>Featured Video</h2>
    <div class="thumb a" role="img" aria-label="City skyline at dusk video preview">
      <svg width="40" height="40" viewBox="0 0 40 40"><circle cx="20" cy="20" r="20" fill="#2b2b2b" opacity=".85"/><polygon points="16,12 28,20 16,28" fill="#fff"/></svg>
    </div>
    <div class="thumb b" role="img" aria-label="Brick downtown building video preview">
      <svg width="40" height="40" viewBox="0 0 40 40"><circle cx="20" cy="20" r="20" fill="#2b2b2b" opacity=".85"/><polygon points="16,12 28,20 16,28" fill="#fff"/></svg>
    </div>
  </section>
  <section class="panel mapsearch">
    <h2>Find your next home using<br>our real estate map search</h2>
    <div class="map" role="img" aria-label="Street map of Charleston with listing pins"></div>
  </section>
  <section class="panel cities">
    <div class="tabs"><div class="tab active">Charleston</div><div class="tab other">Huntington</div></div>
    <div class="city-photo" role="img" aria-label="Downtown office tower at night"></div>
    <p>Whether you are a first time buyer, or a home buying expert, finding and purchasing.</p>
  </section>

  <footer class="footer">
    <span style="left:20px">Quick Links <svg width="10" height="7" viewBox="0 0 10 7"><polyline points="1,1 5,5 9,1" fill="none" stroke="#fff" stroke-width="2"/></svg></span>
    <span style="left:379px">Real Estate <svg width="10" height="7" viewBox="0 0 10 7"><polyline points="1,1 5,5 9,1" fill="none" stroke="#fff" stroke-width="2"/></svg></span>
    <span style="left:740px">Follow us <svg width="10" height="7" viewBox="0 0 10 7"><polyline points="1,1 5,5 9,1" fill="none" stroke="#fff" stroke-width="2"/></svg></span>
    <span style="right:19px">Contact info <svg width="10" height="7" viewBox="0 0 10 7"><polyline points="1,1 5,5 9,1" fill="none" stroke="#fff" stroke-width="2"/></svg></span>
  </footer>
</div>
</body>
</html>
```